Lantern Crest Gathering Day 2021

I am looking to create a flyer for a one day prayer retreat our church is organizing. This flyer will be posted on social media, websites, mobile apps, and will also be printed so it can be mailed to people.

I am looking for something professional, with good use of our logo and band colors (logo colors).

I am counting on the designer's skill, creativity, art and knowledge of media communication to produce a flyer that will effectively and quickly convey the message we are trying to spread.

CONTENT OF THE FLYER:
Event title: Lantern Crest Gathering Day
Date: Tuesday July 2nd, 2021
Time: 11:00AM - 7:00PM
Brindlewick Hotel, 4817 Fennimore Street, Portland, Maine 04102 (Room: Thistlemoor)
Event Key words to highlight what the event is about: Prayer, Fasting, Worship, Prophecy, Revival.
Key phrases:
A one day prayer retreat.
Jesus Chris is Lord

Contact info:
www.velunto.org
Phone: 207 555 0143
Email: contact@quillbrookfold.org

```html
<!DOCTYPE html>
<html lang="en">
<head>
<meta charset="utf-8">
<title>Lantern Crest Gathering Day</title>
<link rel="stylesheet" href="https://fonts.googleapis.com/css2?family=Anton&family=Cinzel:wght@500&family=Open+Sans:wght@600;700;800&display=swap">
<style>
  :root {
    --navy: #0f3660;
    --navy-deep: #082a4f;
    --orange: #f4921f;
    --white: #ffffff;
    --paper: #f2f1f2;
    --ink: #1c1a1b;
    --charcoal: #262324;
    --rule: #cfcfd1;
    --muted: #cfcfcf;
    --stage: #e4e4e5;
  }
  * { margin: 0; padding: 0; box-sizing: border-box; }
  html, body { width: 1040px; height: 1200px; overflow: hidden; background: var(--stage); }
  .flyer {
    position: absolute; left: 70px; top: 20px;
    width: 1086px; height: 1401px;
    transform: scale(0.828); transform-origin: 0 0;
    overflow: hidden; background: var(--paper);
    font-family: "Open Sans", sans-serif;
  }
  .hero-photo {
    position: absolute; left: 0; top: 0; width: 1086px; height: 685px;
    background: radial-gradient(ellipse at 55% 40%, #2a5584 0%, var(--navy) 45%, var(--navy-deep) 100%);
  }
  .prayer-photo {
    position: absolute; left: 563px; top: 536px; width: 523px; height: 865px;
    background:
      radial-gradient(ellipse at 52% 85%, rgba(214,140,60,.55) 0%, rgba(120,70,30,.25) 22%, transparent 45%),
      linear-gradient(180deg, #2b2828 0%, #1f1c1c 55%, #2a2420 100%);
  }
  .brand {
    position: absolute; right: 48px; top: 78px;
    display: flex; align-items: center; gap: 12px;
  }
  .brand-dot { width: 26px; height: 26px; border-radius: 50%; background: var(--orange); }
  .brand-name { font-family: "Cinzel", serif; font-weight: 500; font-size: 46px; color: var(--white); letter-spacing: 1px; }
  .title-rule { position: absolute; left: 195px; top: 208px; width: 7px; height: 200px; background: var(--white); }
  .title { position: absolute; left: 236px; top: 196px; font-weight: 800; line-height: 1; }
  .title-top { display: block; font-size: 80px; color: var(--white); letter-spacing: 1px; }
  .title-main { display: block; font-size: 100px; margin-top: 18px; color: var(--white); letter-spacing: 1px; }
  .title-main .accent { color: var(--orange); }
  .tagline {
    position: absolute; left: 236px; top: 444px;
    font-family: "Cinzel", serif; font-weight: 500; font-size: 28px; color: var(--orange); letter-spacing: .5px;
  }
  .themes { position: absolute; left: 527px; top: 596px; list-style: none; }
  .themes li { display: flex; align-items: center; height: 105px; }
  .theme-badge {
    width: 72px; height: 72px; border-radius: 50%;
    background: var(--orange); border: 3px solid var(--white);
    display: flex; align-items: center; justify-content: center;
  }
  .theme-word { margin-left: 24px; font-size: 50px; font-weight: 700; letter-spacing: 6px; color: var(--white); }
  .theme-word.hot { color: var(--orange); }
  .side-bar { position: absolute; left: 1074px; width: 12px; background: var(--orange); }
  .side-bar.upper { top: 595px; height: 498px; }
  .side-bar.lower { top: 1255px; height: 117px; }
  .details { position: absolute; left: 0; top: 685px; width: 563px; height: 631px; }
  .icon { position: absolute; }
  .date-day { position: absolute; left: 122px; top: 55px; font-family: "Anton", sans-serif; font-size: 140px; line-height: 1; color: var(--ink); }
  .date-month { position: absolute; left: 280px; top: 110px; font-size: 54px; font-weight: 600; color: var(--ink); }
  .divider { position: absolute; left: 58px; width: 472px; height: 1px; background: var(--rule); }
  .time { position: absolute; left: 122px; top: 237px; font-family: "Anton", sans-serif; font-size: 66px; line-height: 1; color: var(--ink); }
  .time-units { position: absolute; left: 133px; top: 315px; font-size: 22px; font-weight: 700; color: var(--ink); word-spacing: 20px; }
  .address { position: absolute; left: 128px; top: 400px; font-size: 29px; font-weight: 600; line-height: 37px; color: var(--ink); font-style: normal; }
  .web-band {
    position: absolute; left: 0; top: 1316px; width: 563px; height: 85px;
    background: var(--orange); color: var(--white);
    display: flex; align-items: center; justify-content: center;
    font-size: 28px; font-weight: 700; letter-spacing: 7px;
  }
  .contact { position: absolute; right: 96px; text-align: right; color: var(--muted); font-weight: 600; }
  .contact.phone { top: 1252px; font-size: 38px; }
  .contact.email { top: 1330px; font-size: 28px; }
  .contact-icon { position: absolute; }
</style>
</head>
<body>
<main class="flyer">
  <div class="hero-photo" role="img" aria-label="Blue-toned photo of a congregation gathered in prayer in a hall"></div>
  <div class="prayer-photo" role="img" aria-label="Dark photo of hands folded in prayer over an open book beside a lit candle"></div>

  <div class="brand"><span class="brand-dot"></span><span class="brand-name">VELUNTO</span></div>

  <div class="title-rule"></div>
  <h1 class="title">
    <span class="title-top">LANTERN CREST</span>
    <span class="title-main"><span class="accent">GATHERING</span> DAY</span>
  </h1>
  <p class="tagline">A ONE DAY PRAYER&nbsp; RETREAT. JESUS CHRIS IS LORD</p>

  <ul class="themes">
    <li><span class="theme-badge"><svg width="34" height="34" viewBox="0 0 34 34" fill="none" stroke="#fff" stroke-width="2"><path d="M17 2v8M14 5h6M17 10l-7 7v14h14V17z M6 31V22l4-3M28 31V22l-4-3M4 31h26M14 31v-6h6v6"/></svg></span><span class="theme-word">PRAYER</span></li>
    <li><span class="theme-badge"><svg width="34" height="34" viewBox="0 0 34 34" fill="none" stroke="#fff" stroke-width="2"><path d="M17 2v8M14 5h6M17 10l-7 7v14h14V17z M6 31V22l4-3M28 31V22l-4-3M4 31h26M14 31v-6h6v6"/></svg></span><span class="theme-word hot">FASTING</span></li>
    <li><span class="theme-badge"><svg width="34" height="34" viewBox="0 0 34 34" fill="none" stroke="#fff" stroke-width="2"><path d="M17 2v8M14 5h6M17 10l-7 7v14h14V17z M6 31V22l4-3M28 31V22l-4-3M4 31h26M14 31v-6h6v6"/></svg></span><span class="theme-word">WORSHIP</span></li>
    <li><span class="theme-badge"><svg width="34" height="34" viewBox="0 0 34 34" fill="none" stroke="#fff" stroke-width="2"><path d="M17 2v8M14 5h6M17 10l-7 7v14h14V17z M6 31V22l4-3M28 31V22l-4-3M4 31h26M14 31v-6h6v6"/></svg></span><span class="theme-word hot">PROPHECY</span></li>
    <li><span class="theme-badge"><svg width="34" height="34" viewBox="0 0 34 34" fill="none" stroke="#fff" stroke-width="2"><path d="M17 2v8M14 5h6M17 10l-7 7v14h14V17z M6 31V22l4-3M28 31V22l-4-3M4 31h26M14 31v-6h6v6"/></svg></span><span class="theme-word">REVIVAL</span></li>
  </ul>
  <div class="side-bar upper"></div>
  <div class="side-bar lower"></div>

  <section class="details">
    <svg class="icon" style="left:48px;top:105px" width="46" height="46" viewBox="0 0 46 46" fill="none" stroke="#f4921f" stroke-width="2.5">
      <rect x="3" y="7" width="40" height="36" rx="2"/><path d="M3 16h40M12 3v8M34 3v8"/>
      <path d="M10 23h4M18 23h4M26 23h4M34 23h2M10 30h4M18 30h4M26 30h4M34 30h2M10 37h4M18 37h4M26 37h4" stroke-width="3"/>
    </svg>
    <div class="date-day">02</div>
    <div class="date-month">July</div>
    <div class="divider" style="top:556px"></div>

    <div class="divider" style="top:223px"></div>
    <svg class="icon" style="left:44px;top:265px" width="56" height="56" viewBox="0 0 56 56" fill="none" stroke="#f4921f" stroke-width="3">
      <path d="M9 20A22 22 0 1 1 7 32"/><path d="M4 12l5 8 8-4"/><path d="M28 16v13h9"/>
    </svg>
    <div class="time">11 - 7</div>
    <div class="time-units">AM - PM</div>
    <div class="divider" style="top:365px"></div>

    <svg class="icon" style="left:50px;top:410px" width="40" height="56" viewBox="0 0 40 56" fill="none" stroke="#f4921f" stroke-width="3">
      <path d="M20 54S3 32 3 20a17 17 0 0 1 34 0c0 12-17 34-17 34z"/><circle cx="20" cy="19" r="5"/>
    </svg>
    <address class="address">Brindlewick Hotel,<br>4817 Fennimore Street,<br>Portland, Maine 04102<br>(Room: Thistlemoor)</address>
  </section>

  <div class="web-band">WWW.VELUNTO.ORG</div>

  <div class="contact phone">207 555 0143</div>
  <svg class="contact-icon" style="left:1002px;top:1260px" width="36" height="36" viewBox="0 0 36 36" fill="none" stroke="#f4921f" stroke-width="2.5">
    <path d="M8 4l6 7-3 4c2 4 6 8 10 10l4-3 7 6-4 5C17 33 3 19 4 8z"/><path d="M21 4a11 11 0 0 1 11 11M21 10a5 5 0 0 1 5 5"/>
  </svg>
  <div class="contact email">contact@quillbrookfold.org</div>
  <svg class="contact-icon" style="left:1007px;top:1340px" width="34" height="26" viewBox="0 0 34 26" fill="none" stroke="#f4921f" stroke-width="2.5">
    <rect x="2" y="2" width="30" height="22"/><path d="M2 3l15 12L32 3"/>
  </svg>
</main>
</body>
</html>
```